Information flyer for 5 day treatment flyer

I am wanting a double sided flyer for my next 5 day treatment program for addictions. I have included the copy for the flyer as an attachment.
I have also included a drop box link to my brand guidelines and my logos. The logo I prefer is the grey horse with the words Willowmere Collective under.
https://www.filecrate.example/sh/k2jtq7wn3xb5lp1/BBQr9TzLm4Kd7c8NpWvY2hsXe?dl=0

https://www.filecrate.example/s/qm8vz2kt6bw9rc4/WILLOWMERE%20COLLECTIVE%20%7C%20Brand%20Identity%20Guidelines.pdf?dl=0
I have also included a copy of an existing flyer which I like very much and a documant with the copy.
https://www.filecrate.example/sh/t7wbn3kx9zq1mv5/CCRt2pLw8-nZ4Kj7FyTuGHs_b?dl=0

I prefer simple, elegant designs please. The design needs to show my clients that I know what I am doing and I am trust worthy and a skilled professional.

Here is the drop box link to the images I have selected for this program. The tones in the images I have selected are orange/red. Please feel free to pick what you think works well.
https://www.filecrate.example/sh/mrq5jv82lnc0tfw/DDDhW392Bx6Lp88_Q7KcZnRye?dl=0

Many thanks
Marisol

```html
<!DOCTYPE html>
<html lang="en">
<head>
<meta charset="utf-8">
<title>Willowmere Collective – 5 Day Intensive Program</title>
<link rel="stylesheet" href="https://fonts.googleapis.com/css2?family=Noto+Sans:wght@400;700;800&family=PT+Sans:wght@700&display=swap">
<style>
  :root {
    --brown: #3f2a1c;
    --brown-deep: #2b1b14;
    --yellow: #f2e55e;
    --orange: #f04e1a;
    --white: #ffffff;
    --ink: #1e1e1e;
    --slate: #56626b;
    --ring: #c6cdcd;
    --wood-dark: #7d6a57;
    --wood-light: #c8bca8;
  }
  * { margin: 0; padding: 0; box-sizing: border-box; }
  html, body { width: 848px; height: 1200px; overflow: hidden; background: var(--brown); }
  body { font-family: "Noto Sans", sans-serif; color: var(--white); }
  .flyer { position: relative; width: 848px; height: 1200px; background: var(--brown); overflow: hidden; }

  .shape { position: absolute; left: 0; top: 0; }

  .outcomes-title {
    position: absolute; left: 89px; top: 44px;
    font-family: "Noto Sans", sans-serif; font-weight: 800;
    font-size: 21.8px; letter-spacing: 0.3px; color: var(--yellow); white-space: nowrap;
  }
  .outcomes {
    position: absolute; left: 113px; top: 91px; list-style: none;
    font-size: 15.2px; line-height: 18.4px; white-space: nowrap;
  }
  .outcomes li { position: relative; margin-bottom: 2.6px; }
  .outcomes li::before {
    content: ""; position: absolute; left: -22px; top: 4px;
    width: 10px; height: 10px; border-radius: 50%; background: var(--orange);
  }
  .outcomes li.plain::before { display: none; }

  .photo { position: absolute; left: 0; top: 0; }

  .brand-seal {
    position: absolute; left: 51px; top: 448px; width: 146px; height: 146px;
    border-radius: 50%; background: var(--brown-deep); border: 3px solid var(--ring);
    display: flex; align-items: center; justify-content: center;
  }
  .brand-seal span {
    font-size: 8.6px; letter-spacing: 1.6px; color: var(--ring); text-align: center; line-height: 13px;
  }

  .section-title {
    font-family: "PT Sans", sans-serif; font-weight: 700; font-size: 16px;
    color: var(--slate); letter-spacing: 0.3px; white-space: nowrap;
  }
  .block { position: absolute; color: var(--ink); font-size: 12.2px; }
  .dot-list { list-style: none; margin-top: 7px; white-space: nowrap; }
  .dot-list li { position: relative; padding-left: 18px; line-height: 18.4px; }
  .dot-list li::before {
    content: ""; position: absolute; left: 0; top: 4px;
    width: 9px; height: 9px; border-radius: 50%; background: var(--ink);
  }

  .inclusions { left: 78px; top: 740px; }
  .investment { left: 78px; top: 896px; display: flex; align-items: baseline; gap: 9px; }
  .investment .price { font-size: 17px; color: var(--orange); white-space: nowrap; }
  .terms { left: 78px; top: 934px; }

  .program { left: 462px; top: 729px; }
  .program .when { font-size: 14.5px; margin-top: 6px; margin-bottom: 2px; }
  .program .session { line-height: 18.4px; white-space: nowrap; }

  .enrolment { left: 462px; top: 901px; width: 321px; }
  .enrolment p { line-height: 18.4px; text-align: justify; margin-top: 7px; }
  .enrolment p + p { margin-top: 9px; }

  .footer { position: absolute; font-size: 12px; color: var(--white); line-height: 19px; white-space: nowrap; }
  .footer-left { left: 40px; top: 1130px; }
  .footer-left strong { font-weight: 700; letter-spacing: 0.3px; }
  .footer-right { right: 48px; top: 1134px; text-align: right; }
</style>
</head>
<body>
<main class="flyer">

  <h1 class="outcomes-title">DURING THIS 12 DAY INTENSIVE PROGRAM YOU WILL:</h1>
  <ul class="outcomes">
    <li>Identify what you need to do for yourself to stop destructive relationship<br>patterns.</li>
    <li>Learn how to protect yourself from feeling overwhelmed or drained in close<br>relationships.</li>
    <li>Release emotional baggage from past adult relationships.</li>
    <li class="plain">Significantly heal childhood abandonment and engulfment issues.</li>
    <li>Identify the subconscious negative beliefs that are sabotaging you from<br>having the relationship you desire.</li>
    <li class="plain">Release childhood trauma out of your body from abuse and neglect</li>
    <li>Learn how to set healthy boundaries - physically, emotionally, spiritually,<br>intellectually and sexually.</li>
    <li>Differentiate between needs and values - the drivers in relationships.</li>
    <li>Identify your needs and values and determine steps to take to meet them.</li>
    <li class="plain">Free yourself of shame, guilt and fear from childhood and adult relationships.</li>
    <li>Communicate your needs and ask for what you want without feeling too<br>embarrassed or vulnerable.</li>
  </ul>

  <svg class="photo" width="848" height="1200" viewBox="0 0 848 1200" role="img" aria-label="Photograph of a young child sitting against a weathered timber wall, head resting on folded arms">
    <defs>
      <linearGradient id="wood" x1="0" y1="0" x2="1" y2="0.3">
        <stop offset="0" stop-color="var(--wood-light)"/>
        <stop offset="0.45" stop-color="#a89580"/>
        <stop offset="1" stop-color="var(--wood-dark)"/>
      </linearGradient>
    </defs>
    <path d="M20,660 C150,560 330,470 520,455 C650,445 760,380 825,268 L825,660 C740,692 600,708 420,700 C300,695 150,705 20,724 Z" fill="url(#wood)"/>
  </svg>

  <svg class="shape" width="848" height="1200" viewBox="0 0 848 1200" aria-hidden="true">
    <path d="M20,724 C150,705 300,695 420,700 C600,708 740,692 825,655 L825,1114 L20,1114 Z" fill="var(--white)"/>
  </svg>

  <div class="brand-seal"><span>WILLOWMERE<br>COLLECTIVE</span></div>

  <section class="block inclusions">
    <h2 class="section-title">INCLUSIONS</h2>
    <ul class="dot-list">
      <li>A pre-assessment phone consult</li>
      <li>Relevant on online diagnostic survey’s</li>
      <li>Integrated Equine Assisted Psychotherapy</li>
      <li>Ropes course</li>
      <li>All course materials (notebook, writing materials),<br>Morning and afternoon tea daily,</li>
    </ul>
  </section>

  <section class="block investment">
    <h2 class="section-title">INVESTMENTS :</h2>
    <span class="price">$2250 including GST</span>
  </section>

  <section class="block terms">
    <h2 class="section-title">TERMS &amp; CONDITIONS</h2>
    <ul class="dot-list">
      <li>A non-refundable deposit of $500 is required to<br>hold your place.</li>
      <li>Enrolments with full payment is required by<br>Tuesday, 23th October 2018.</li>
      <li>Charge card transactions incur a 3.3% merchant fee,<br>other credit cards 2.5%.</li>
      <li>Card payment facility available.</li>
    </ul>
  </section>

  <section class="block program">
    <h2 class="section-title">PROGRAM DETAILS</h2>
    <p class="when">WHEN</p>
    <p class="session">Thursday 25th October 6:00pm – 9:00pm</p>
    <p class="session">Friday, 26th October 9:00pm – 5:00pm</p>
    <p class="session">Saturday, 27th October 9:00pm – 9:00pm</p>
    <p class="session">Sunday, 28th October 9:00pm – 5:00pm</p>
    <p class="session">Monday, 29th October 9:00pm – 4:00pm</p>
  </section>

  <section class="block enrolment">
    <h2 class="section-title">ENROLMENT PROCESS</h2>
    <p>This 5 day program is limited in numbers and offers individual and group time. Enrolments close Friday, 19th October 2018.</p>
    <p>To book your place, register your interest or find out more about this program please call<br>Marisol 0400 555 218</p>
    <p>Out of town participants please contact our office for assistance with accommodation if required.</p>
  </section>

  <footer class="footer footer-left">
    <strong>The Willowmere Collective Pty Ltd.</strong><br>
    ABN 12 345 678 901<br>
    18 Banksia Lane, Oakvale NSW 2790
  </footer>
  <footer class="footer footer-right">
    Phone: 0400 555 218<br>
    Email: marisol@willowmerecollective.example
  </footer>

</main>
</body>
</html>
```